Business Card Design

We are a residential half way house for the addict ,the alcoholic and dual diagnosed in recovery.
i house both men and woman age 18+

Industry/Entity Type

Residential

```html
<!DOCTYPE html>
<html lang="en">
<head>
<meta charset="UTF-8">
<title>Harbor Light Sober Living – Business Card</title>
<link rel="stylesheet" href="https://fonts.googleapis.com/css2?family=Quicksand:wght@300;400&display=swap">
<style>
  :root {
    --page-bg: #1b1b1b;
    --card-dark: #232323;
    --card-light: #3a3a3a;
    --accent-red: #c43a2c;
    --accent-red-light: #d4503f;
    --text-main: #d9d9d9;
    --text-muted: #8c8c8c;
    --divider: #b8362a;
  }
  * { margin: 0; padding: 0; box-sizing: border-box; }
  html, body {
    width: 1200px;
    height: 900px;
    overflow: hidden;
    background: var(--page-bg);
  }
  .canvas {
    position: relative;
    width: 1200px;
    height: 900px;
    display: flex;
    align-items: center;
    justify-content: center;
  }
  .business-card {
    position: relative;
    width: 1000px;
    height: 572px;
    background: linear-gradient(135deg, var(--card-dark) 0%, var(--card-light) 55%, var(--card-dark) 100%);
    font-family: "Quicksand", sans-serif;
    font-weight: 300;
    color: var(--text-main);
    overflow: hidden;
  }
  .identity {
    position: absolute;
    right: 560px;
    top: 196px;
    text-align: left;
    width: 300px;
  }
  .identity-name {
    font-size: 28px;
    font-weight: 300;
    letter-spacing: 0.5px;
    color: var(--text-main);
    margin-bottom: 18px;
  }
  .identity-role {
    font-size: 19px;
    line-height: 1.2;
    color: var(--text-muted);
    padding-left: 8px;
  }
  .divider {
    position: absolute;
    left: 468px;
    top: 110px;
    width: 1px;
    height: 350px;
    background: var(--divider);
  }
  .contact-list {
    position: absolute;
    left: 500px;
    top: 150px;
    list-style: none;
  }
  .contact-item {
    display: flex;
    align-items: flex-start;
    gap: 14px;
    font-size: 19px;
    line-height: 1.25;
    margin-bottom: 30px;
    color: var(--text-main);
  }
  .contact-icon {
    flex: 0 0 18px;
    width: 18px;
    height: 18px;
    margin-top: 2px;
  }
  .contact-icon path,
  .contact-icon rect,
  .contact-icon circle { fill: none; stroke: var(--text-muted); stroke-width: 1.4; }
  .accent-band {
    position: absolute;
    right: 0;
    top: 40px;
    width: 120px;
    height: 494px;
    background: linear-gradient(180deg, var(--accent-red) 0%, var(--accent-red-light) 100%);
    border-radius: 6px 0 0 6px;
  }
</style>
</head>
<body>
<main class="canvas">
  <section class="business-card" aria-label="Harbor Light Sober Living business card">
    <div class="identity">
      <h1 class="identity-name">Marisa Delgado Owner</h1>
      <p class="identity-role">Addiction recovery<br>5 years in recovery</p>
    </div>

    <div class="divider"></div>

    <ul class="contact-list">
      <li class="contact-item">
        <svg class="contact-icon" viewBox="0 0 18 18" aria-hidden="true">
          <path d="M4 2 L7 2 L8 6 L6 7.5 C7 10 8 11 10.5 12 L12 10 L16 11 L16 14 C16 15 15 16 14 16 C7 16 2 11 2 4 C2 3 3 2 4 2 Z"/>
        </svg>
        <span>(555) 014-2270; (555) 014-2271<br>Fax: (555) 018-3904</span>
      </li>
      <li class="contact-item">
        <svg class="contact-icon" viewBox="0 0 18 18" aria-hidden="true">
          <rect x="2" y="4" width="14" height="10"/>
          <path d="M2 4 L9 10 L16 4"/>
        </svg>
        <span>marisadelgado@example.com</span>
      </li>
      <li class="contact-item">
        <svg class="contact-icon" viewBox="0 0 18 18" aria-hidden="true">
          <path d="M9 17 C5 12 3 9.5 3 7 A6 6 0 0 1 15 7 C15 9.5 13 12 9 17 Z"/>
          <circle cx="9" cy="7" r="2"/>
        </svg>
        <span>Harbor Light Sober Living Inc.<br>2740 Palm Grove Rd. Seabrook,Fla<br>33400</span>
      </li>
    </ul>

    <div class="accent-band"></div>
  </section>
</main>
</body>
</html>
```